Brindle Works Australia Website

Brindle Works Australia (BWA) is a Industrial, Mining & Transport Services provider in Australia. We require a website that is both pc and mobile freindly. The website will be used to both present our company services and give us exposure in a crowded market. The main page of the website will have a snapshot of who BWA is and its from this page that the user can click to enter the area of interest ie. Industrial, Mining and Transport. A disticted logo can be used to indicate the area in question.<br/>Within the industrial, Mining and the Transport services pages will need list and description of services that are provided, current customer lists and news pages.<br/>The website will need a contacts page so prospective customers can get in contact with BWA.<br/>The website design will require a user freindly back end so future updates and ammendments can be carriedout by less experienced people within the BWA business.

Target Market(s)

Industrial, Mining and Transport Services provider markets

Coding

Coded - Design and coding required

Number of Pages Required

5+ page

Font styles to use
Sans Serif

Colors
00a990

Requirements
Must have
• Ability to build servises with in services. because the main service area is only the main service with in each service group there is alot of smaller services / tasks.
• Key wording for easy seach engine capabilities. The website will need to be search engine freindly.

```html
<!DOCTYPE html>
<html lang="en">
<head>
<meta charset="utf-8">
<title>Brindle Works Australia — Mining and Transport Services</title>
<link rel="stylesheet" href="https://fonts.googleapis.com/css2?family=Poppins:ital,wght@0,300;0,400;0,500;0,600;0,700;1,400&display=swap">
<style>
:root{
  --green:#00a990;
  --dark:#231f20;
  --dark-2:#2a2627;
  --ink:#222;
  --muted:#777;
  --line:#e4e4e4;
  --soft:#f2f2f2;
  --white:#fff;
  --chip:#4a4546;
}
*{margin:0;padding:0;box-sizing:border-box}
html,body{width:1200px;height:5199px;overflow:hidden}
body{font-family:'Poppins',sans-serif;color:var(--ink);background:var(--white);position:relative}
.abs{position:absolute}
a{color:inherit;text-decoration:none}

.topbar{top:0;left:0;width:1200px;height:36px;background:var(--dark);color:#fff;font-size:13px}
.topbar .phone{position:absolute;left:0;top:0;width:282px;height:36px;background:var(--green);clip-path:polygon(0 0,100% 0,94% 100%,0 100%);padding:9px 0 0 86px}
.topbar .dots{position:absolute;left:712px;top:13px;display:flex;gap:60px}
.topbar .dots span{width:10px;height:10px;border-radius:50%;background:#fff}
.topbar .login{position:absolute;left:958px;top:0;width:136px;height:36px;background:#3a3536;font-size:11px;font-weight:500;text-align:center;padding-top:10px}

.header{top:36px;left:0;width:1200px;height:103px;background:#fff}
.brand{position:absolute;left:88px;top:24px;display:flex;align-items:center;gap:10px}
.brand .mark{width:16px;height:16px;background:var(--green)}
.brand .name{font-weight:700;font-size:17px;color:var(--green);line-height:1.05;text-transform:uppercase}
.brand .sub{display:block;font-size:8px;color:var(--green);letter-spacing:.3px;margin-top:4px}
.nav{position:absolute;left:541px;top:45px;display:flex;gap:38px;font-size:12px;font-weight:500}
.nav .active{color:var(--green);border-bottom:2px solid var(--green);padding-bottom:3px}
.search{position:absolute;left:1088px;top:42px}

.hero{top:139px;left:0;width:1200px;height:620px;background:
  radial-gradient(ellipse at 75% 25%,#5a4634 0%,transparent 45%),
  radial-gradient(ellipse at 35% 80%,#8a4a16 0%,transparent 40%),
  linear-gradient(90deg,#1c1612 0%,#2c2119 55%,#3a2d22 100%);color:#fff}
.hero .pre{position:absolute;left:85px;top:178px;font-size:31px;font-weight:400}
.hero h1{position:absolute;left:82px;top:198px;font-size:110px;font-weight:600;letter-spacing:1px}
.hero p{position:absolute;left:86px;top:328px;width:470px;font-size:14px;line-height:22px}
.btn{display:inline-block;font-size:11px;font-weight:600;text-transform:uppercase;text-align:center}
.hero .btn{position:absolute;left:86px;top:396px;width:150px;height:42px;background:#fff;color:var(--ink);padding-top:14px}
.hero .slide-line{position:absolute;left:1153px;top:218px;width:2px;height:121px;background:rgba(255,255,255,.35)}
.hero .slide-line::before{content:"";position:absolute;left:0;top:0;width:2px;height:58px;background:#fff}

.about-bg{top:759px;left:884px;width:316px;height:613px;background:#e9e9e9;overflow:hidden}
.about-bg .word{position:absolute;left:90px;top:600px;transform:rotate(-90deg);transform-origin:0 0;font-size:150px;font-weight:700;color:#cfcfcf;letter-spacing:4px}
.about-photo{top:851px;left:686px;width:391px;height:428px;background:linear-gradient(160deg,#8e9aa4 0%,#b9a37a 55%,#d8b23a 100%);box-shadow:30px 40px 60px rgba(0,0,0,.15)}
.about-photo::before{content:"";position:absolute;left:0;top:0;width:156px;height:138px;background:#fff}
.about-photo::after{content:"";position:absolute;left:0;top:0;width:152px;height:134px;background:linear-gradient(160deg,#7d8a95,#9aa4aa)}
.eyebrow{font-size:13px;font-weight:500;color:var(--green);text-transform:uppercase}
.about-text{top:928px;left:86px;width:480px}
.about-text h2{font-size:36px;font-weight:400;line-height:40px;margin-top:12px}
.about-text p{font-size:14px;line-height:23px;color:#333;margin-top:22px}
.about-text .btn{margin-top:24px;width:150px;height:42px;background:#e6e6e6;padding-top:14px}

.section-title{left:0;width:1200px;text-align:center;font-size:36px;font-weight:400}
.section-title::after{content:"";display:block;width:42px;height:1px;background:#bbb;margin:10px auto 0}

.services{top:1485px;left:0;width:1200px;height:793px;display:grid;grid-template-columns:400px 400px 400px;grid-template-rows:397px 396px}
.svc{position:relative;color:#fff;padding:40px 0 0 62px}
.svc.dark{background:var(--dark-2)}
.svc.green{background:var(--green)}
.svc .icon{height:100px;display:flex;align-items:flex-end}
.svc h3{font-size:22px;font-weight:600;line-height:25px;text-transform:uppercase;margin-top:34px;width:310px}
.svc p{font-size:12px;line-height:20px;width:280px;margin-top:10px;opacity:.9}
.svc .more{display:inline-flex;align-items:center;gap:8px;margin-top:22px;border:2px solid #fff;height:42px;padding:0 18px;font-size:11px;font-weight:500;text-transform:uppercase}
.photo{position:relative}
.ph-mining{background:linear-gradient(180deg,#d7b48a 0%,#a87a4b 55%,#5a3f28 100%)}
.ph-refinery{background:linear-gradient(180deg,#4b3a3a 0%,#c7763a 45%,#e6a054 60%,#3a3030 100%)}
.ph-truck{background:linear-gradient(110deg,#e09a3a 0%,#c83a22 45%,#5a3a2a 100%)}

.features{top:2371px;left:87px;width:1026px;display:flex}
.feature{width:274px}
.feature .ficon{height:52px}
.feature h4{font-size:13px;font-weight:500;line-height:20px;text-transform:uppercase;margin-top:24px;width:160px}
.feature p{font-size:12px;line-height:18px;color:var(--muted);margin-top:12px;width:215px}
.divider{top:2625px;left:87px;width:1026px;height:1px;background:var(--line)}

.project{top:2789px;height:391px;color:#fff}
.project span{position:absolute;left:0;right:0;bottom:30px;text-align:center;font-size:22px;font-weight:500}
.pj-1{left:89px;width:238px;background:linear-gradient(180deg,#8fb0cf 0%,#dfe6ea 30%,#3f5a4a 60%,#2a3a30 100%)}
.pj-2{left:339px;width:523px;background:linear-gradient(180deg,#cfd3d6 0%,#8c9094 45%,#3b3d3f 100%)}
.pj-3{left:874px;width:238px;background:linear-gradient(180deg,#6a5a60 0%,#b47a5a 50%,#3a3436 100%)}
.dots{top:3205px;left:577px;display:flex;gap:10px;align-items:center}
.dots i{width:8px;height:8px;border-radius:50%;border:1px solid #aaa}
.dots i.on{width:12px;height:12px;border:2px solid #555}

.testimonials{top:3303px;left:0;width:1200px;height:587px;background:var(--soft)}
.testimonials .eyebrow{position:absolute;top:90px;left:0;width:1200px;text-align:center}
.testimonials h2{position:absolute;top:112px;left:0;width:1200px;text-align:center;font-size:36px;font-weight:400}
.quote-mark{position:absolute;left:86px;top:232px;font-size:220px;line-height:1;color:#e0e0e0;font-weight:700;font-family:Georgia,serif}
.quote{position:absolute;left:86px;top:332px;width:520px;font-size:17px;line-height:31px;font-style:italic;color:#444}
.quote-name{position:absolute;left:86px;top:443px;font-size:13px;font-weight:600;color:var(--green);text-transform:uppercase}
.arrows{position:absolute;left:86px;top:488px}
.tri{position:absolute;left:672px;top:175px}
.person{position:absolute;left:760px;top:178px;width:270px;height:322px;background:linear-gradient(180deg,#e8e8e8 0%,#9a9a9a 45%,#6e6e6e 100%)}

.blog-eyebrow{top:3985px;left:0;width:1200px;text-align:center}
.blog-title{top:4006px}
.post{top:4076px;width:500px;height:464px;background:#fff;box-shadow:0 6px 30px rgba(0,0,0,.08)}
.post .thumb{position:absolute;left:16px;top:20px;width:468px;height:238px}
.post .tag{position:absolute;left:16px;bottom:12px;background:#fff;font-size:10px;font-weight:600;padding:3px 7px;text-transform:uppercase}
.post .meta{position:absolute;left:36px;top:285px;font-size:9px;color:#999;text-transform:uppercase}
.post h3{position:absolute;left:36px;top:305px;font-size:20px;font-weight:600;text-transform:uppercase}
.post p{position:absolute;left:36px;top:350px;width:430px;font-size:12px;line-height:20px;color:#555}
.post .views{position:absolute;left:36px;top:405px;display:flex;gap:6px;align-items:center;font-size:13px;font-weight:500;color:var(--green)}
.th-1{background:linear-gradient(180deg,#3a2e22 0%,#b0783a 40%,#7a6a5a 70%,#4a3f38 100%)}
.th-2{background:linear-gradient(180deg,#3a4a5a 0%,#8a8f96 45%,#b83a3a 65%,#5a5a5a 100%)}
.interest{top:4586px;left:0;width:1200px;text-align:center;font-size:12px;font-weight:600;text-transform:uppercase}
.interest a{color:var(--green)}

.footer{top:4758px;left:0;width:1200px;height:441px;background:var(--dark);color:#fff}
.newsletter{top:4685px;left:0;width:541px;height:145px;background:var(--green)}
.newsletter .field{position:absolute;left:89px;top:43px;width:363px;height:56px;background:#fff;display:flex;align-items:center}
.newsletter .field span{flex:1;font-size:11px;color:#666;padding-left:18px;display:flex;gap:8px;align-items:center}
.newsletter .field b{width:45px;height:56px;background:var(--dark);display:flex;align-items:center;justify-content:center}
.f-brand{top:4938px;left:90px;display:flex;align-items:center;gap:10px;color:#fff}
.f-brand .mark{width:16px;height:16px;background:#fff}
.f-brand .name{font-weight:700;font-size:19px;line-height:1.05;text-transform:uppercase}
.f-brand .sub{display:block;font-size:9px;margin-top:5px}
.f-social{top:5041px;left:145px;display:flex;gap:9px}
.f-social i{width:30px;height:30px;border-radius:50%;background:var(--chip)}
.f-col{top:4890px;color:#fff}
.f-col h5{font-size:13px;font-weight:500;text-transform:uppercase;margin-bottom:22px}
.f-col li{list-style:none;font-size:11px;line-height:27px}
.contact-item{display:flex;gap:10px;font-size:11px;line-height:16px;margin-bottom:14px}
.copyright{top:5162px;left:0;width:1200px;text-align:center;font-size:11px;color:#fff}
.totop{top:5127px;left:1132px;width:40px;height:40px;border-radius:50%;background:var(--green);display:flex;align-items:center;justify-content:center}
</style>
</head>
<body>

<div class="abs topbar">
  <div class="phone">&#9742; +08 (123)-555-0142</div>
  <div class="dots" aria-label="Social links"><span></span><span></span><span></span><span></span></div>
  <div class="login">LOGIN / REGISTER</div>
</div>

<header class="abs header">
  <div class="brand"><span class="mark"></span><span class="name">Brindle Works<br>Australia<span class="sub">Mining and Transport Services</span></span></div>
  <nav class="nav">
    <a class="active">HOME</a><a>ABOUT US</a><a>PROJECTS</a><a>FEATURE</a><a>BLOG</a><a>CONTACT</a>
  </nav>
  <svg class="search" width="22" height="22" viewBox="0 0 22 22"><circle cx="9" cy="9" r="7" fill="none" stroke="#222" stroke-width="2"/><line x1="14" y1="14" x2="20" y2="20" stroke="#222" stroke-width="2"/></svg>
</header>

<section class="abs hero" role="img" aria-label="Worker grinding metal with sparks flying in a dark workshop">
  <div class="pre">Industrial Works</div>
  <h1>Services.</h1>
  <p>Lorem ipsum dolor sit ametcon sectetur adipisicing elit, sed dolusmod tempor incidi labore et...</p>
  <a class="btn">Find our more</a>
  <div class="slide-line"></div>
</section>

<div class="abs about-bg"><span class="word">ABOUT</span></div>
<div class="abs about-photo" role="img" aria-label="Yellow hard hat on an excavation site with a digger"></div>
<section class="abs about-text">
  <div class="eyebrow">About us</div>
  <h2>Short inroduction about our campany</h2>
  <p>Lorem ipsum dolor sit ametcon sectetur adipisicing elit, sed doiusmod tempor incidi labore et dolore magna aliqua. Ut enim ad mini veniam, quis nostrud exercitation ullamco laboris nisi ut aliquip ex ea commodo consequat. Duis aute irure dolor in reprehenderit in voluptate velit esse cillum dolore eu fugiat nulla pariatur.</p>
  <a class="btn">Find our more</a>
</section>

<h2 class="abs section-title" style="top:1400px">Our Services</h2>

<section class="abs services">
  <div class="svc dark">
    <div class="icon"><svg width="76" height="100" viewBox="0 0 76 100"><rect x="2" y="60" width="70" height="38" fill="#00a990"/><rect x="50" y="22" width="10" height="40" fill="#00a990"/><circle cx="60" cy="12" r="8" fill="#00a990"/><circle cx="70" cy="6" r="5" fill="#00a990"/><polygon points="2,60 2,46 24,60 24,46 46,60" fill="#00a990"/><rect x="10" y="72" width="10" height="8" fill="#2a2627"/><rect x="28" y="72" width="10" height="8" fill="#2a2627"/><rect x="46" y="72" width="10" height="8" fill="#2a2627"/></svg></div>
    <h3>BWA Industrial Services Division</h3>
    <p>Offers an integrated site service and main-tenance of your fixed plant. Our team are experienced in developing</p>
    <a class="more">Read more <svg width="16" height="8" viewBox="0 0 16 8"><path d="M0 4h14M11 1l3 3-3 3" stroke="#fff" fill="none"/></svg></a>
  </div>
  <div class="photo ph-mining" role="img" aria-label="Mining loader beside a crane and earth pile"></div>
  <div class="svc dark">
    <div class="icon"><svg width="120" height="90" viewBox="0 0 120 90"><rect x="2" y="30" width="50" height="40" fill="#00a990"/><rect x="56" y="10" width="60" height="60" rx="4" fill="#00a990"/><rect x="66" y="20" width="16" height="14" fill="#2a2627"/><circle cx="22" cy="78" r="9" fill="#00a990"/><circle cx="80" cy="78" r="9" fill="#00a990"/><circle cx="100" cy="78" r="9" fill="#00a990"/></svg></div>
    <h3>BWA Transport Division</h3>
    <p>Specialises in the transportation of all types of materials such as, Steel, Structural Steel, Concrete Building Panels, Machinery...</p>
    <a class="more">Read more <svg width="16" height="8" viewBox="0 0 16 8"><path d="M0 4h14M11 1l3 3-3 3" stroke="#fff" fill="none"/></svg></a>
  </div>
  <div class="photo ph-refinery" role="img" aria-label="Refinery towers at sunset"></div>
  <div class="svc green">
    <div class="icon"><svg width="136" height="76" viewBox="0 0 136 76"><rect x="20" y="8" width="34" height="30" fill="#fff"/><rect x="26" y="14" width="20" height="14" fill="#00a990"/><rect x="10" y="34" width="90" height="16" fill="#fff"/><polygon points="100,38 132,60 118,66 100,50" fill="#fff"/><rect x="4" y="52" width="100" height="20" rx="10" fill="#fff"/><circle cx="20" cy="62" r="5" fill="#00a990"/><circle cx="40" cy="62" r="5" fill="#00a990"/><circle cx="60" cy="62" r="5" fill="#00a990"/><circle cx="80" cy="62" r="5" fill="#00a990"/></svg></div>
    <h3>BWA Mining Services Division</h3>
    <p>Offers an integrated service in equipment rental, maintenance &amp; earthmoving. Suppor-ted by a modern and comprehensive...</p>
    <a class="more">Read more <svg width="16" height="8" viewBox="0 0 16 8"><path d="M0 4h14M11 1l3 3-3 3" stroke="#fff" fill="none"/></svg></a>
  </div>
  <div class="photo ph-truck" role="img" aria-label="Red truck cab in golden light"></div>
</section>

<section class="abs features">
  <div class="feature">
    <div class="ficon"><svg width="62" height="44" viewBox="0 0 62 44"><circle cx="31" cy="12" r="9" fill="#222"/><circle cx="12" cy="16" r="7" fill="#00a990"/><circle cx="50" cy="16" r="7" fill="#00a990"/><path d="M14 44a17 17 0 0 1 34 0z" fill="#222"/><path d="M0 40a12 12 0 0 1 20-9v9z M62 40a12 12 0 0 0-20-9v9z" fill="#00a990"/></svg></div>
    <h4>Qualified Electricians</h4>
    <p>Aenean sollicitudin lorem quis bibendum auctor nisi...</p>
  </div>
  <div class="feature">
    <div class="ficon"><svg width="44" height="52" viewBox="0 0 44 52"><path d="M8 14a14 14 0 0 1 28 0z" fill="#222"/><rect x="4" y="14" width="36" height="4" fill="#222"/><circle cx="22" cy="24" r="8" fill="#222"/><path d="M4 52a18 18 0 0 1 36 0z" fill="#222"/><circle cx="22" cy="42" r="6" fill="#00a990"/></svg></div>
    <h4>We Provide</h4>
    <p>Aenean sollicitudin lorem quis bibendum auctor nisi...</p>
  </div>
  <div class="feature">
    <div class="ficon"><svg width="52" height="52" viewBox="0 0 52 52"><circle cx="26" cy="26" r="20" fill="none" stroke="#222" stroke-width="10" stroke-dasharray="8 5"/><circle cx="26" cy="26" r="16" fill="#222"/><path d="M18 26l6 6 10-12" stroke="#00a990" stroke-width="4" fill="none"/></svg></div>
    <h4>Expert Electrical Solutions</h4>
    <p>Aenean sollicitudin lorem quis bibendum auctor nisi...</p>
  </div>
  <div class="feature">
    <div class="ficon"><svg width="56" height="54" viewBox="0 0 56 54"><rect x="2" y="6" width="40" height="38" rx="3" fill="none" stroke="#222" stroke-width="4"/><rect x="2" y="6" width="40" height="9" fill="#222"/><rect x="9" y="20" width="6" height="6" fill="#222"/><rect x="19" y="20" width="6" height="6" fill="#222"/><rect x="9" y="30" width="6" height="6" fill="#222"/><circle cx="42" cy="40" r="12" fill="#fff" stroke="#00a990" stroke-width="4"/><path d="M42 33v7h5" stroke="#00a990" stroke-width="3" fill="none"/></svg></div>
    <h4>Prompt Reliable Service</h4>
    <p>Aenean sollicitudin lorem quis bibendum auctor nisi...</p>
  </div>
</section>
<div class="abs divider"></div>

<h2 class="abs section-title" style="top:2707px">Our Projects</h2>
<div class="abs project pj-1" role="img" aria-label="Truck on a mountain road under snowy peaks"><span>Heading here</span></div>
<div class="abs project pj-2" role="img" aria-label="Steel tanks and towers of an industrial plant"><span>Heading goes here</span></div>
<div class="abs project pj-3" role="img" aria-label="Tower crane against a dusky sky"><span>Heading here</span></div>
<div class="abs dots"><i class="on"></i><i></i><i></i></div>

<section class="abs testimonials">
  <div class="eyebrow">Customer</div>
  <h2>Client’s Testimonials</h2>
  <div class="quote-mark">“</div>
  <p class="quote">Aenean sollicitudin, lorem quis bibendum auctor, nisi elit nec sagittis sem nibh id elittate cursus a sit amet mauris morbi accumsan ipsum velit &nbsp;tellus a odio...</p>
  <div class="quote-name">- Dana Ortiz</div>
  <svg class="arrows" width="80" height="24" viewBox="0 0 80 24"><path d="M22 12H2M8 6l-6 6 6 6" stroke="#999" fill="none" stroke-width="1.5"/><path d="M34 12h42M70 6l6 6-6 6" stroke="#222" fill="none" stroke-width="1.5"/></svg>
  <svg class="tri" width="475" height="330" viewBox="0 0 475 330"><polygon points="0,0 0,325 475,325" fill="#00a990"/></svg>
  <div class="person" role="img" aria-label="Client portrait in a white cap and denim jacket"></div>
</section>

<div class="abs eyebrow blog-eyebrow">Blog</div>
<h2 class="abs section-title blog-title">Latest Blog Posts</h2>
<article class="abs post" style="left:89px">
  <div class="thumb th-1" role="img" aria-label="Interior of an industrial plant with beams and lights"><span class="tag">News</span></div>
  <div class="meta">By: Admin &nbsp;• &nbsp;On 19th April 2018</div>
  <h3>Some blog heading here...</h3>
  <p>Imperdiet etiam ultricies nisi vel augue curabitur ullamcor per ultricies nisi nam eget dui etiam rhoncus maecenas tempus..</p>
  <div class="views"><svg width="18" height="12" viewBox="0 0 18 12"><path d="M1 6c4-7 12-7 16 0-4 7-12 7-16 0z" fill="#00a990"/><circle cx="9" cy="6" r="2.5" fill="#fff"/></svg>153</div>
</article>
<article class="abs post" style="left:609px">
  <div class="thumb th-2" role="img" aria-label="Red truck parked beside a trailer"><span class="tag">News</span></div>
  <div class="meta">By: Admin &nbsp;• &nbsp;On 19th April 2018</div>
  <h3>Some blog heading here...</h3>
  <p>Imperdiet etiam ultricies nisi vel augue curabitur ullamcor per ultricies nisi nam eget dui etiam rhoncus maecenas tempus..</p>
  <div class="views"><svg width="18" height="12" viewBox="0 0 18 12"><path d="M1 6c4-7 12-7 16 0-4 7-12 7-16 0z" fill="#00a990"/><circle cx="9" cy="6" r="2.5" fill="#fff"/></svg>153</div>
</article>
<div class="abs interest">Interested in my blogs? <a>Check out more</a></div>

<footer class="abs footer"></footer>
<div class="abs newsletter">
  <div class="field"><span><svg width="12" height="9" viewBox="0 0 12 9"><rect x=".5" y=".5" width="11" height="8" fill="none" stroke="#00a990"/><path d="M.5.5l5.5 4 5.5-4" stroke="#00a990" fill="none"/></svg>Enter your email address...</span><b><svg width="14" height="14" viewBox="0 0 14 14"><path d="M1 6l12-5-4 12-2-5z" fill="#fff"/></svg></b></div>
</div>
<div class="abs f-brand"><span class="mark"></span><span class="name">Brindle Works<br>Australia<span class="sub">Mining and Transport Services</span></span></div>
<div class="abs f-social" aria-label="Social links"><i></i><i></i><i></i></div>

<div class="abs f-col" style="left:442px">
  <h5>Quick Links</h5>
  <ul><li>Home</li><li>About Us</li><li>Projects</li><li>Feature</li><li>Latest Blog Post</li><li>Contact Us</li></ul>
</div>
<div class="abs f-col" style="left:684px">
  <h5>Information</h5>
  <ul><li>About Us</li><li>Delivery</li><li>Store</li><li>Terms &amp; Conditions</li><li>Policies</li><li>Shop Instagram</li></ul>
</div>
<div class="abs f-col" style="left:908px">
  <h5>Contact Us</h5>
  <div class="contact-item"><svg width="12" height="9" viewBox="0 0 12 9"><rect width="12" height="9" fill="#00a990"/><path d="M0 0l6 5 6-5" stroke="#231f20" fill="none"/></svg><div>Email:<br>hello@brindleworks.example</div></div>
  <div class="contact-item"><svg width="12" height="12" viewBox="0 0 12 12"><path d="M2 1l3 0 1 3-2 1a7 7 0 0 0 3 3l1-2 3 1v3c-6 0-10-4-10-9z" fill="#00a990"/></svg><div>Phone:<br>+08 123-555-0142</div></div>
  <div class="contact-item"><svg width="12" height="14" viewBox="0 0 12 14"><path d="M6 14S1 8 1 5a5 5 0 0 1 10 0c0 3-5 9-5 9z" fill="#00a990"/><circle cx="6" cy="5" r="2" fill="#231f20"/></svg><div>Office Location:<br>Some address line goes here</div></div>
</div>
<div class="abs copyright">© COPYRIGHT 2019. ALL RIGHTS RESERVED</div>
<div class="abs totop"><svg width="12" height="14" viewBox="0 0 12 14"><path d="M6 13V1M1 6l5-5 5 5" stroke="#fff" fill="none" stroke-width="1.5"/></svg></div>

</body>
</html>
```